Global Outreach Fellowship needs a Book Cover Design Project

I am a pastor, missionary, author, and the founder of a non-profit organization. I am in the process of publishing a book focused on "The Spirit of a Faithful Shepherd" and desire a contemporary, even somewhat abstract book cover. Here is a link to the company's web page portfolio that designed our Web Page, to give you an idea of the style of cover that I am looking for. http://www.pixelharborstudio.com/cd-covers

Though the book is obviously targeted toward Christians, I want it to be attractive enough to capture the attention of the general population as well.

Industry/Entity Type

Non-Profit

```html
<!DOCTYPE html>
<html lang="en">
<head>
<meta charset="utf-8">
<title>The Spirit of a Faithful Shepherd — Book Cover</title>
<link rel="stylesheet" href="https://fonts.googleapis.com/css2?family=Cinzel:wght@400&family=Pinyon+Script&family=Tinos&display=swap">
<style>
  :root {
    --page: #ffffff;
    --sky-deep: #2c2f86;
    --sky-mid: #1f6aac;
    --sky-teal: #1b86ad;
    --sky-light: #3f9fd2;
    --spine: #231f20;
    --ink-light: #ffffff;
    --band: rgba(20, 60, 110, 0.4);
  }
  * { margin: 0; padding: 0; box-sizing: border-box; }
  html, body {
    width: 1200px; height: 949px; overflow: hidden;
    background: var(--page);
  }
  .spread {
    position: absolute; left: 64px; top: 58px;
    width: 1088px; height: 816px;
  }
  .back-cover, .front-cover { position: absolute; top: 0; height: 816px; overflow: hidden; }
  .back-cover { left: 0; width: 524px; }
  .front-cover { left: 565px; width: 523px; }
  .spine {
    position: absolute; left: 524px; top: 0; width: 41px; height: 816px;
    background: var(--spine);
  }
  .sky-photo { position: absolute; inset: 0; }
  .back-cover .sky-photo {
    background: linear-gradient(180deg, var(--sky-light) 0%, var(--sky-mid) 45%, var(--sky-teal) 100%);
  }
  .front-cover .sky-photo {
    background: linear-gradient(180deg, var(--sky-deep) 0%, var(--sky-mid) 35%, var(--sky-teal) 65%, var(--sky-deep) 100%);
  }
  .title-band {
    position: absolute; left: 0; top: 208px; width: 523px; height: 290px;
    background: var(--band);
  }
  .blurb {
    position: absolute; left: 48px; top: 250px; width: 395px;
    font-family: "Tinos", "Times New Roman", serif;
    font-size: 13.5px; line-height: 20px; color: var(--ink-light);
  }
  .isbn-box {
    position: absolute; left: 48px; top: 687px; width: 176px; height: 93px;
    background: var(--page);
  }
  .spine-title, .spine-author {
    position: absolute; left: 50%; white-space: nowrap; color: var(--ink-light);
    transform-origin: 0 0;
  }
  .spine-title {
    top: 26px;
    font-family: "Tinos", "Times New Roman", serif; font-size: 19px;
    transform: rotate(90deg) translateY(-50%);
  }
  .spine-author {
    top: 512px;
    font-family: "Cinzel", "Times New Roman", serif; font-size: 14px; letter-spacing: 6px;
    transform: rotate(90deg) translateY(-50%);
  }
  .book-title {
    position: absolute; left: 0; top: 270px; width: 523px; padding-left: 20px; text-align: center;
    font-family: "Pinyon Script", cursive; font-weight: 400;
    font-size: 56px; line-height: 76px; color: var(--ink-light);
    text-shadow: 2px 3px 4px rgba(0,0,0,0.55);
  }
  .book-title .small { font-size: 42px; }
  .front-author {
    position: absolute; left: 0; top: 766px; width: 523px; text-align: center;
    font-family: "Cinzel", "Times New Roman", serif; font-size: 16px; letter-spacing: 3.5px;
    color: var(--ink-light);
  }
</style>
</head>
<body>
<main class="spread">
  <section class="back-cover">
    <div class="sky-photo" role="img" aria-label="Photograph of a blue sky with clouds and sunlight"></div>
    <p class="blurb">Lorem ipsum dolor sit amet, consectetur adipisicing elit, sed do eiusmod tempor incididunt ut labore et dolore magna aliqua. Ut enim ad minim veniam, quis nostrud exercitation ullamco laboris nisi ut aliquip ex ea commodo consequat. Duis aute irure dolor in reprehenderit in voluptate velit esse cillum dolore eu fugiat nulla pariatur. Excepteur sint occaecat cupidatat non proident, sunt in culpa qui officia deserunt mollit anim id est laborum.<br>Duis aute irure dolor in reprehenderit in voluptate velit esse cillum dolore eu fugiat nulla pariatur. Excepteur sint occaecat cupidatat non proident, sunt in culpa qui officia deserunt mollit anim id est laborum.</p>
    <div class="isbn-box"></div>
  </section>

  <section class="spine">
    <span class="spine-title">The Spirit of a Faithful Shepherd</span>
    <span class="spine-author">AUTHORS NAME HERE</span>
  </section>

  <section class="front-cover">
    <div class="sky-photo" role="img" aria-label="Photograph of a blue sky with clouds, sunlight and a faint globe"></div>
    <div class="title-band"></div>
    <h1 class="book-title">The Spirit <span class="small">of a</span><br>Faithful Shepherd</h1>
    <p class="front-author">AUTHORS NAME HERE</p>
  </section>
</main>
</body>
</html>
```